Local Realtors helping sellers and buyers make the right decision

Looking for an Ad to place in our local paper, that is completely different from the traditional ads we see from realtors. My mother and I are a team and we would like to really stand out from the rest of the ads. Ideally, one that has humor in it would be great. Being that it's the largest investment most people make in their lives, we want to show that hiring us is going to be the best move sellers and buyers will make. With over 50 years of experience as full time realtors between us. We want buyers and sellers to know that they don't just hire their friend or the first realtor they meet. You'll be hiring two full time agents that are in the trenches everyday and know how to help them navigate the ever changing market.
I'm attaching some meme's that I've seen online to give you an idea of what we're looking for in regards to being funny, yet professional. I am also attaching two typical ads that are in this newspaper. We promoting ourselves as Agents, and not homes specifically in this ad. Our head shots will be used as well as our company logo and other contact information. The size of the ad we have reserved is ( 1/2 page vertical (4.7 x 12.25 inches) Please let me know what else I you may need to help

Gregory Halvern Sales Associate greghomes@ravelmail.net Immediate Response # (555) 318-6047 Brookline Ridge Office 417 Marlow Street (555) 690-2174 Ashcombe, ME 04815 Carol Halvern Sales Associate cmhalvern58@ravelmail.net Immediate Response # (555) 827-4390 Brookline Ridge Office 417 Marlow Street (555) 690-2174 Ashcombe, ME 04815

Target Market(s)

Seller's and Buyers of residential property

Industry/Entity Type

Real Estate

Font styles to use
Serif

Colors
0555a3

Requirements
Must have
• Powerful, yet funny message to our targets
Nice to have
• We would like the ad to attract sellers and buyers
Should not have
• Should not be unprofessional. I know that's a broad description, but if you have to think about it not being professional, then it probably shouldn't be in there...

```html
<!DOCTYPE html>
<html lang="en">
<head>
<meta charset="utf-8">
<title>Local Realtors Ad</title>
<link href="https://fonts.googleapis.com/css2?family=Bebas+Neue&family=Roboto+Condensed:ital,wght@0,400;0,700;1,400&display=swap" rel="stylesheet">
<style>
  :root {
    --navy: #0b1c82;
    --yellow: #ffe600;
    --white: #ffffff;
    --page: #f2f2f2;
    --ink: #1a1a1a;
    --photo-light: #d9dadc;
    --photo-dark: #6e6a66;
  }
  html, body {
    margin: 0;
    padding: 0;
    width: 1200px;
    height: 973px;
    overflow: hidden;
    background: var(--page);
  }
  .ad {
    position: absolute;
    left: 420px;
    top: 16px;
    width: 360px;
    height: 940px;
    background: var(--white);
    box-shadow: 0 6px 14px rgba(0,0,0,0.25);
    overflow: hidden;
    font-family: "Roboto Condensed", sans-serif;
  }
  .hero-photo {
    position: absolute;
    left: 0; top: 0;
    width: 360px; height: 500px;
    background: linear-gradient(160deg, #8c8c8c 0%, var(--photo-light) 35%, #b9b4ae 60%, var(--photo-dark) 100%);
  }
  .headline {
    position: absolute;
    left: 24px; top: 22px;
    margin: 0;
    font-family: "Bebas Neue", sans-serif;
    font-weight: 400;
    line-height: 0.9;
    text-shadow: 0 1px 3px rgba(0,0,0,0.35);
  }
  .headline span { display: block; }
  .headline .lead { color: var(--white); font-size: 62px; }
  .headline .sub { color: var(--white); font-size: 46px; margin-bottom: 4px; }
  .headline .big { color: var(--yellow); font-size: 61px; }
  .headline .mid { color: var(--yellow); font-size: 48px; }
  .band {
    position: absolute;
    left: 0; top: 0;
  }
  .agent {
    position: absolute;
    left: 25px;
    width: 320px;
    height: 130px;
  }
  .agent.first { top: 526px; }
  .agent.second { top: 707px; }
  .headshot {
    position: absolute;
    left: 0; top: 0;
    width: 94px; height: 124px;
    border: 3px solid var(--white);
    background: linear-gradient(180deg, #3f5a2e 0%, #7d8f6a 45%, #5a6f92 100%);
    box-shadow: 0 2px 6px rgba(0,0,0,0.4);
  }
  .agent.second .headshot {
    background: linear-gradient(180deg, #8e9a82 0%, #c9c3b0 45%, #7f9fd0 100%);
  }
  .agent-info {
    position: absolute;
    left: 117px; top: 0;
    color: var(--white);
  }
  .agent-name {
    margin: 0;
    font-family: "Bebas Neue", sans-serif;
    font-weight: 400;
    font-size: 27px;
    line-height: 1;
    color: var(--yellow);
  }
  .agent-title {
    margin: 1px 0 8px;
    font-style: italic;
    font-size: 12px;
    letter-spacing: 0.2px;
  }
  .contact {
    list-style: none;
    margin: 0; padding: 0;
    font-size: 12px;
    line-height: 1.3;
  }
  .contact li {
    position: relative;
    padding-left: 19px;
    margin-bottom: 3px;
  }
  .contact svg {
    position: absolute;
    left: 0; top: 3px;
  }
  .divider {
    position: absolute;
    left: 25px; top: 684px;
    width: 310px; height: 1px;
    background: linear-gradient(90deg, rgba(255,255,255,0.05), rgba(255,255,255,0.45), rgba(255,255,255,0.05));
  }
  .footer {
    position: absolute;
    left: 0; top: 862px;
    width: 360px; height: 78px;
    background: var(--white);
  }
  .brand {
    position: absolute;
    left: 27px; top: 22px;
    display: flex;
    align-items: center;
    gap: 6px;
    font-weight: 700;
    font-size: 15px;
    color: var(--navy);
    text-transform: uppercase;
  }
  .brand .mark {
    width: 14px; height: 14px;
    background: var(--navy);
  }
  .badges {
    position: absolute;
    right: 22px; top: 16px;
    display: flex;
    gap: 22px;
  }
  .badge {
    width: 36px; height: 40px;
    background: var(--ink);
  }
  .badge.round { border-radius: 4px; background: #3a3a3a; }
</style>
</head>
<body>
  <article class="ad">
    <div class="hero-photo" role="img" aria-label="Photo of a businessman in a grey suit thinking, finger on chin, in front of a blurred office building"></div>

    <h1 class="headline">
      <span class="lead">Local Realtors</span>
      <span class="sub">Helping Sellers and</span>
      <span class="big">Buyers</span>
      <span class="big">Make</span>
      <span class="mid">The Right</span>
      <span class="mid">Decision</span>
    </h1>

    <svg class="band" width="360" height="862" viewBox="0 0 360 862" aria-hidden="true">
      <path d="M0 437 Q190 545 360 428 L360 862 L0 862 Z" fill="var(--navy)"/>
      <path d="M0 437 Q190 545 360 428" fill="none" stroke="var(--white)" stroke-width="4"/>
    </svg>

    <section class="agent first">
      <div class="headshot" role="img" aria-label="Headshot of Gregory Halvern"></div>
      <div class="agent-info">
        <h2 class="agent-name">Gregory Halvern</h2>
        <p class="agent-title">SALES ASSOCIATE</p>
        <ul class="contact">
          <li><svg width="11" height="8" viewBox="0 0 11 8"><rect width="11" height="8" fill="var(--yellow)"/><path d="M0 0 L5.5 4.5 L11 0" fill="none" stroke="var(--navy)" stroke-width="1"/></svg>greghomes@ravelmail.net</li>
          <li><svg width="10" height="10" viewBox="0 0 10 10"><path d="M2 0 L4 2.5 L3 4 Q4.5 6 6 7 L7.5 6 L10 8 L8.5 10 Q2 9 0 1.5 Z" fill="var(--yellow)"/></svg># (555) 318-6047</li>
          <li><svg width="8" height="11" viewBox="0 0 8 11"><path d="M4 11 L0.6 5.5 A4 4 0 1 1 7.4 5.5 Z" fill="var(--yellow)"/><circle cx="4" cy="4" r="1.5" fill="var(--navy)"/></svg>Brookline Ridge Office<br>417 Marlow Street (555) 690-2174<br>Ashcombe, ME 04815</li>
        </ul>
      </div>
    </section>

    <div class="divider"></div>

    <section class="agent second">
      <div class="headshot" role="img" aria-label="Headshot of Carol Halvern"></div>
      <div class="agent-info">
        <h2 class="agent-name">Carol Halvern</h2>
        <p class="agent-title">SALES ASSOCIATE</p>
        <ul class="contact">
          <li><svg width="11" height="8" viewBox="0 0 11 8"><rect width="11" height="8" fill="var(--yellow)"/><path d="M0 0 L5.5 4.5 L11 0" fill="none" stroke="var(--navy)" stroke-width="1"/></svg>cmhalvern58@ravelmail.net</li>
          <li><svg width="10" height="10" viewBox="0 0 10 10"><path d="M2 0 L4 2.5 L3 4 Q4.5 6 6 7 L7.5 6 L10 8 L8.5 10 Q2 9 0 1.5 Z" fill="var(--yellow)"/></svg># (555) 827-4390</li>
          <li><svg width="8" height="11" viewBox="0 0 8 11"><path d="M4 11 L0.6 5.5 A4 4 0 1 1 7.4 5.5 Z" fill="var(--yellow)"/><circle cx="4" cy="4" r="1.5" fill="var(--navy)"/></svg>Brookline Ridge Office<br>417 Marlow Street (555) 690-2174<br>Ashcombe, ME 04815</li>
        </ul>
      </div>
    </section>

    <footer class="footer">
      <div class="brand"><span class="mark"></span>Harborline Realty</div>
      <div class="badges">
        <div class="badge" role="img" aria-label="Membership badge"></div>
        <div class="badge round" role="img" aria-label="Housing badge"></div>
      </div>
    </footer>
  </article>
</body>
</html>
```